Pale Lantern Double Sided Flyer Design

We need a double sided flyer (1/3 of an A4 which is 99mm x 210mm) developed for our Newcastle(NSW) tour. This flyer will be placed in tourist information centres and hotels. We want it to direct people to our website or be able to make bookings over the phone.

About Us:-
We are a city walking tour company that runs tours day or night. We run both day and night and will incorporate real history / real Pale lantern. Some of the stories will be quite serious i.e.- there are infamous murders from 100 years ago, baffling court cases, even a bit of poetry written by murderers, suicides, love triangles, you name it. We will be telling the historical stories that tourists will not hear from any other tour provider. A bit of darkness, a bit of mystery and a bit of history theme.

We do no go for scares and let the very real stories deliver the entertainment for our guests. Our customers enjoy our tours, but it isn't light fun and frivolity. Our stories are being carefully crafted and are packed with unexpected twists, turns; revelations whilst remaining all 100% true. We deliver deep, rich, engaging stories.

Here are a few samples of quotes from the characters in our stories that may give you an idea of the kind of history we will cover:-

"There were bits of spines, bits of skulls, [and] finger bones spilled out all over the streets - I ended up filling three boxes. Children were playing with them for weeks”

"I had a close shave last night and now I want a close haircut.”

“She's a beautiful child', isn't she? She's the cause of all the trouble.”

“I did it because she would not come home with me.”

"I have killed my wife. I’m glad she’s dead.”

"Stand aside or I'll put a bullet through both of you."

“You villain, I'll teach you to take away my character."

“You’re not dead yet, you bastard!”

Our website, booking form and contact details can be viewed at www.palelantern.com.au

Target Market(s)

Tourists

Industry/Entity Type

Tour

Colors

Designer to choose colors to be used in the design.

Requirements
Must have
• Vertical orientation please.
• Please also include a reference to a discount offer of 25% using the promo code "WICK".
Nice to have
• FRONT FLYER INFORMATION
• - Pale Lantern Logo
• - "I have killed my wife; I'm glad she's dead."
• - Harbourside Hidden Lanes Walk
• - 25% Discount Offer Codeword WICK
• - web address at the base; www.palelantern.com.au
• BACK FLYER INFORMATION
• - "She's a beautiful child', isn't she? She's the cause of all the trouble.
• - Pale Lantern Logo at the base along with the web address www.palelantern.com.au
• - Blurb:- Pale lantern brings back Newcastle's hidden past, the forgotten past, the dark past that may not want to be remembered.
• Real stories from the streets around you. Discover the histories you won't hear anywhere else. The forgotten stories of yesteryear finally get a chance to be told. Through you they get to live again.
Should not have
• GENERAL
• Please do not include the phone number, email address or social media icons. We want to drive online bookings.

```html
<!DOCTYPE html>
<html lang="en">
<head>
<meta charset="utf-8">
<title>Pale Lantern Flyer – Front and Back</title>
<link href="https://fonts.googleapis.com/css2?family=Montserrat:wght@400;500;600;700&family=Open+Sans:wght@400;600&display=swap" rel="stylesheet">
<style>
  :root{
    --bg:#efe9df;
    --paper:#ffffff;
    --ink:#2b2b2b;
    --ink-soft:#555555;
    --red:#e0262b;
    --band:#3b3b3b;
    --band-light:#6a6a6a;
    --photo-light:#d9d9d9;
    --photo-mid:#8a8a8a;
    --photo-dark:#262626;
  }
  *{box-sizing:border-box;margin:0;padding:0}
  html,body{width:800px;height:1200px;overflow:hidden}
  body{background:var(--bg);font-family:"Montserrat",sans-serif;color:var(--ink);position:relative}

  .flyer{position:absolute;top:218px;width:360px;height:764px;background:var(--paper);overflow:hidden;box-shadow:0 4px 14px rgba(0,0,0,.18)}
  .flyer--front{left:30px}
  .flyer--back{left:410px}

  .photo{position:absolute;left:0;width:100%}
  .photo--street{top:150px;height:430px;background:linear-gradient(180deg,var(--photo-light) 0%,var(--photo-mid) 35%,var(--photo-dark) 70%,#4a4a4a 100%)}
  .photo--skyline{top:0;height:380px;background:linear-gradient(180deg,#f2f2f2 0%,#d0d0d0 38%,#5e5a58 55%,#2e2c2b 78%,#6f6f6f 100%)}

  .shapes{position:absolute;inset:0;width:100%;height:100%}

  .brand{position:absolute;left:0;width:100%;display:flex;justify-content:center;align-items:center;gap:8px}
  .brand__mark{width:14px;height:14px;background:var(--red)}
  .brand__name{font-weight:600;color:var(--ink);letter-spacing:1px;text-transform:uppercase;line-height:1}
  .flyer--front .brand{top:98px}
  .flyer--front .brand__name{font-size:26px}
  .flyer--back .brand{top:650px}
  .flyer--back .brand__name{font-size:20px}

  .quote{position:absolute;left:0;width:100%;text-align:center;font-weight:500;color:var(--ink);line-height:1.15}
  .quote em{font-style:normal;color:var(--red)}
  .quote--front{top:580px;font-size:21px}
  .quote--front .mark{color:var(--red);font-size:24px;font-weight:700;vertical-align:-2px}
  .quote--back{top:392px;font-size:20px}
  .quote--back .caps{text-transform:uppercase}

  .tour-title{position:absolute;top:642px;left:0;width:100%;text-align:center;line-height:1.1;text-transform:uppercase;font-weight:600}
  .tour-title__lead{display:block;color:var(--red);font-size:18px}
  .tour-title__rest{display:block;color:var(--ink);font-size:17px}

  .offer{position:absolute;top:694px;left:75px;width:210px;height:44px;background:var(--red);border-radius:8px;box-shadow:0 3px 6px rgba(0,0,0,.35);color:#fff;text-align:center;padding-top:4px}
  .offer__tag{position:absolute;top:-9px;left:-6px;background:var(--band);color:#fff;font-size:9px;font-weight:700;padding:2px 6px}
  .offer__main{font-size:17px;font-weight:600;text-transform:uppercase;line-height:1.2}
  .offer__main b{font-size:22px;font-weight:700}
  .offer__code{font-size:8px;font-weight:600}

  .web{position:absolute;left:0;width:100%;text-align:center;color:#eeeeee;font-size:10px;line-height:12px;letter-spacing:2.5px;text-transform:uppercase}
  .flyer--front .web{top:749px}
  .flyer--back .web{top:749px}

  .blurb{position:absolute;top:494px;left:26px;right:26px;font-family:"Open Sans",sans-serif;font-size:8.6px;line-height:1.35;color:var(--ink-soft)}
  .blurb__label{color:var(--red);font-weight:600;font-size:10px;text-transform:uppercase}
  .blurb p{padding:3px 0}
  .blurb p + p{border-top:1px solid #cfcfcf;margin-top:4px;padding-top:6px}
  .blurb__rule{border-top:1px solid #cfcfcf;margin-bottom:4px}

  .pull-line{position:absolute;top:600px;left:0;width:100%;text-align:center;line-height:1.15}
  .pull-line__lead{display:block;color:var(--red);font-size:18px;font-weight:600;text-transform:uppercase}
  .pull-line__rest{display:block;color:var(--ink);font-size:16px;font-weight:500}

  .booking-note{position:absolute;top:732px;left:0;width:100%;text-align:center;color:#fff;font-size:10px;line-height:12px;font-weight:600}
</style>
</head>
<body>

<section class="flyer flyer--front" aria-label="Flyer front">
  <div class="photo photo--street" role="img" aria-label="Misty black and white photograph of an old tram on a rainy street with a lone figure"></div>
  <svg class="shapes" viewBox="0 0 360 764" aria-hidden="true">
    <path d="M0 572 Q 170 452 360 470 L360 764 L0 764 Z" fill="var(--paper)"/>
    <path d="M0 566 Q 170 445 360 463" fill="none" stroke="var(--red)" stroke-width="5"/>
    <path d="M0 558 Q 170 439 360 456" fill="none" stroke="var(--band)" stroke-width="1.5"/>
    <path d="M0 748 Q 220 746 360 706 L360 764 L0 764 Z" fill="var(--band)"/>
    <path d="M0 743 Q 220 741 360 701" fill="none" stroke="var(--red)" stroke-width="2.5"/>
    <line x1="60" y1="636" x2="300" y2="636" stroke="#bdbdbd" stroke-width="1"/>
  </svg>

  <div class="brand"><span class="brand__mark"></span><span class="brand__name">Pale Lantern</span></div>

  <p class="quote quote--front"><span class="mark">“</span>I have <em>killed</em> my wife,<br>I'm glad she's <em>dead</em><span class="mark">”</span></p>

  <h1 class="tour-title"><span class="tour-title__lead">Harbourside Hidden Lanes</span><span class="tour-title__rest">Walk</span></h1>

  <div class="offer">
    <span class="offer__tag">GET</span>
    <div class="offer__main"><b>25%</b> Discount</div>
    <div class="offer__code">Offer Codeword "WICK"</div>
  </div>

  <p class="web">www.palelantern.com.au</p>
</section>

<section class="flyer flyer--back" aria-label="Flyer back">
  <div class="photo photo--skyline" role="img" aria-label="Black and white photograph of the city skyline with a clock tower above dark trees"></div>
  <svg class="shapes" viewBox="0 0 360 764" aria-hidden="true">
    <path d="M0 400 Q 180 300 360 318 L360 764 L0 764 Z" fill="var(--paper)"/>
    <path d="M0 394 Q 180 292 360 310" fill="none" stroke="var(--red)" stroke-width="5"/>
    <path d="M0 386 Q 180 285 360 302" fill="none" stroke="var(--band)" stroke-width="1.5"/>
    <path d="M0 726 Q 220 722 360 690 L360 764 L0 764 Z" fill="var(--band)"/>
    <path d="M0 721 Q 220 717 360 685" fill="none" stroke="var(--red)" stroke-width="2.5"/>
    <line x1="90" y1="746" x2="270" y2="746" stroke="var(--band-light)" stroke-width="1"/>
  </svg>

  <p class="quote quote--back">She's a <em>beautiful child</em>,<br>isn't she?<br>She's the cause of<br><span class="caps">All the <em>trouble.</em></span></p>

  <div class="blurb">
    <div class="blurb__rule"></div>
    <p><span class="blurb__label">Blurb:</span><br>Pale lantern brings back Newcastle's hidden past, the forgotten past, the dark past that may not want to be remembered.</p>
    <p>Real stories from the streets around you. Discover the histories you won't hear anywhere else. The forgotten stories of yesteryear finally get a chance to be told. Through you they get to live again.</p>
  </div>

  <p class="pull-line"><span class="pull-line__lead">You villain, I'll teach you</span><span class="pull-line__rest">to take away my character</span></p>

  <div class="brand"><span class="brand__mark"></span><span class="brand__name">Pale Lantern</span></div>

  <p class="booking-note">Booking form and contact details can be viewed at</p>
  <p class="web">www.palelantern.com.au</p>
</section>

</body>
</html>
```